Roof wash and Gutter Cleaning

Would like to see our colors and logo incorporated into design along with phone number and before/after picture(s). We use a non pressure softwash process we use unlike high pressure. We are a exterior cleaning company that likes to set our standards high with safe methods to cleaning the everyday surfaces on homes.
“Serving the Tri-State Area”
A list of our services:
House washing
Shingle and metal roof washing
Deck cleaning
Window cleaning
Concrete cleaning
Gutter cleaning
415-362-0917
We do not need the address section as these will be more for our meet and greets. As well handed out as clipped door  postcards.

Target Market(s)
Shingle roof wash and gutter cleaning
Look and feel

```html
<!DOCTYPE html>
<html lang="en">
<head>
<meta charset="utf-8">
<title>Crestline Exterior Cleaning – Postcard</title>
<link href="https://fonts.googleapis.com/css2?family=Nunito+Sans:wght@400;700&family=Montserrat:wght@500;600&display=swap" rel="stylesheet">
<style>
  :root{
    --blue:#2f63b6;
    --sky:#6aa8dc;
    --green:#5cb947;
    --gray-text:#5d5d5d;
    --label:#444;
    --card-back:#e6e7e8;
    --circle-a:#5b9be0;
    --circle-b:#2f6cc0;
  }
  *{margin:0;padding:0;box-sizing:border-box}
  html,body{width:1200px;height:1132px;overflow:hidden;background:#fff}
  body{position:relative;font-family:"Nunito Sans",Arial,sans-serif}
  .spec-label{position:absolute;right:140px;font-family:"Montserrat",Arial,sans-serif;font-style:italic;font-size:11px;letter-spacing:1.5px;color:#333}
  .card{position:absolute;left:133px;width:927px;height:412px;overflow:hidden}
  .card--front{top:124px;background:radial-gradient(ellipse 62% 75% at 50% 55%,#fff 0%,#fff 30%,#cfe3f5 60%,var(--sky) 100%)}
  .card--back{top:591px;background:var(--card-back)}
  .service-icon{position:absolute;width:80px;height:80px;border-radius:50%;background:radial-gradient(circle at 35% 30%,var(--circle-a),var(--circle-b));border:2px solid #eaf3fc}
  .service-icon svg{position:absolute;left:0;top:0;width:76px;height:76px;fill:none;stroke:#fff;stroke-width:2;stroke-linecap:round;stroke-linejoin:round}
  .service{position:absolute;line-height:1}
  .service--left{text-align:right}
  .service .small{display:block;font-size:16px;color:var(--gray-text)}
  .service .big{display:block;font-size:27px;font-weight:700;color:var(--blue)}
  .brand{position:absolute;left:0;width:927px;top:172px;text-align:center;font-size:66px;font-weight:700;color:var(--blue);line-height:1}
  .brand-dot{display:inline-block;width:30px;height:30px;border-radius:50%;background:var(--green);margin-right:14px;vertical-align:8px}
  .tagline{position:absolute;left:304px;width:320px;top:314px;text-align:center;font-size:19px;color:#8a8a8a;padding-bottom:10px;border-bottom:1.5px solid #9a9a9a}
  .phone{position:absolute;display:flex;align-items:center;font-family:"Montserrat",Arial,sans-serif;font-weight:600;color:var(--blue);letter-spacing:4px;white-space:nowrap}
  .phone svg{flex:none}
  .photo{position:absolute;width:148px;height:120px}
  .tag{position:absolute;font-family:"Montserrat",Arial,sans-serif;font-size:11px;letter-spacing:3.5px;color:var(--label)}
  .divider{position:absolute;width:1px;background:#9a9a9a}
  .back-brand{position:absolute;left:712px;top:262px;width:200px;text-align:center}
  .back-brand .name{font-size:40px;font-weight:700;color:var(--blue);line-height:1}
  .back-brand .sub{font-size:10px;color:#7a7a7a;margin-top:6px}
</style>
</head>
<body>

<p class="spec-label" style="top:102px">post card front - size - 9x4 inch</p>

<section class="card card--front">
  <div class="service service--left" style="right:628px;top:70px"><span class="small">house</span><span class="big">washing</span></div>
  <div class="service-icon" style="left:311px;top:57px">
    <svg viewBox="0 0 80 80"><path d="M22 40 L40 24 L56 38"/><path d="M26 36 V50 H52 V36"/><rect x="35" y="40" width="8" height="10"/><path d="M18 58 C26 54 34 54 42 57 L56 52 C60 51 62 55 58 57 L44 64 H22"/><path d="M57 18 v8 M53 22 h8"/></svg>
  </div>

  <div class="service service--left" style="right:724px;top:155px"><span class="small">deck</span><span class="big">cleaning</span></div>
  <div class="service-icon" style="left:215px;top:131px">
    <svg viewBox="0 0 80 80"><path d="M34 14 V48"/><path d="M26 48 H42 L46 62 H22 Z"/><path d="M26 55 v7 M32 55 v7 M38 55 v7"/><path d="M46 40 H60 L58 62 H48 Z"/><path d="M48 40 C48 32 58 32 58 40"/><circle cx="54" cy="30" r="3"/><path d="M18 30 v6 M15 33 h6"/></svg>
  </div>

  <div class="service service--left" style="right:760px;top:252px"><span class="small">gutter</span><span class="big">cleaning</span></div>
  <div class="service-icon" style="left:174px;top:228px">
    <svg viewBox="0 0 80 80"><path d="M20 40 L46 18"/><path d="M44 16 l6 6"/><rect x="40" y="38" width="20" height="22" rx="3"/><path d="M40 46 H60"/><circle cx="44" cy="62" r="3"/><circle cx="56" cy="62" r="3"/><circle cx="18" cy="46" r="2"/><circle cx="24" cy="52" r="2"/><circle cx="16" cy="56" r="2"/><circle cx="26" cy="60" r="2"/></svg>
  </div>

  <div class="service-icon" style="left:573px;top:29px">
    <svg viewBox="0 0 80 80"><rect x="18" y="16" width="36" height="44"/><path d="M36 16 V60 M22 20 H50 V56 H22 Z"/><path d="M27 27 v6 M24 30 h6 M44 44 v6 M41 47 h6"/><path d="M56 36 h6 v6 l4 4 V62 H52 V46 l4 -4 Z"/><path d="M58 32 h6"/></svg>
  </div>
  <div class="service" style="left:662px;top:52px"><span class="small">window</span><span class="big">cleaning</span></div>

  <div class="service-icon" style="left:657px;top:128px">
    <svg viewBox="0 0 80 80"><path d="M16 40 L34 24 L50 38"/><path d="M20 36 V60 H46 V38"/><rect x="24" y="42" width="8" height="8"/><rect x="36" y="48" width="6" height="12"/><path d="M46 34 L60 20"/><rect x="56" y="14" width="10" height="10" rx="2" transform="rotate(45 61 19)"/><path d="M18 18 l4 4 M22 18 l-4 4 M62 36 v5 M59.5 38.5 h5"/></svg>
  </div>
  <div class="service" style="left:748px;top:135px"><span class="small">shingle and</span><span class="small" style="margin-left:5px">metal</span><span class="big" style="margin-left:5px">roof</span><span class="big">washing</span></div>

  <div class="service-icon" style="left:628px;top:229px">
    <svg viewBox="0 0 80 80"><path d="M30 14 H38 V38"/><path d="M38 38 L30 56"/><path d="M22 58 H40"/><ellipse cx="50" cy="48" rx="12" ry="14"/><circle cx="50" cy="50" r="5"/><circle cx="50" cy="50" r="1.5"/><path d="M44 36 C46 30 54 30 56 36"/></svg>
  </div>
  <div class="service" style="left:716px;top:257px"><span class="small">concrete</span><span class="big">cleaning</span></div>

  <div class="brand"><span class="brand-dot"></span>Crestline</div>
  <div class="tagline">Exterior Cleaning &amp; Maintenance Co.</div>

  <div class="phone" style="left:298px;top:354px;font-size:31px">
    <svg width="32" height="32" viewBox="0 0 32 32" style="margin-right:10px"><circle cx="16" cy="16" r="15" fill="var(--green)"/><path d="M11 8c1-.5 2 0 2.5 1l1.2 2.6c.3.8 0 1.6-.6 2l-1 .7c.8 1.9 2.3 3.5 4.2 4.4l.8-1c.5-.6 1.3-.8 2-.5l2.6 1.2c.9.5 1.3 1.5.9 2.4l-.5 1c-.6 1.2-2 1.8-3.3 1.4C14.6 22 10 17.4 8.9 12.2c-.3-1.3.2-2.7 1.4-3.4z" fill="var(--blue)"/></svg>
    415-362-0917
  </div>
</section>

<p class="spec-label" style="top:571px">post card back - size - 9x4 inch</p>

<section class="card card--back">
  <span class="tag" style="left:137px;top:55px">BEFORE</span>
  <span class="tag" style="left:226px;top:55px">AFTER</span>
  <span class="tag" style="left:470px;top:55px">BEFORE</span>
  <span class="tag" style="left:559px;top:55px">AFTER</span>
  <div class="divider" style="left:213px;top:54px;height:138px"></div>
  <div class="divider" style="left:546px;top:54px;height:138px"></div>

  <div class="photo" role="img" aria-label="Two-storey house with porch before washing" style="left:53px;top:72px;background:linear-gradient(180deg,#b9bcc0 0%,#8d8478 45%,#6b5f50 70%,#3e4a30 100%)"></div>
  <div class="photo" role="img" aria-label="Same house after washing" style="left:225px;top:72px;background:linear-gradient(180deg,#c2c5c8 0%,#958c80 45%,#7a6b58 70%,#3e4a30 100%)"></div>
  <div class="photo" role="img" aria-label="Shingle roof with vent before cleaning" style="left:386px;top:72px;background:linear-gradient(180deg,#8a8378 0%,#6f6a64 45%,#5b5955 100%)"></div>
  <div class="photo" role="img" aria-label="Shingle roof with vent after cleaning" style="left:558px;top:72px;background:linear-gradient(180deg,#8a8378 0%,#7c7a77 45%,#6e6d6b 100%)"></div>
  <div class="photo" role="img" aria-label="Metal roof half cleaned, green panels" style="left:729px;top:72px;height:118px;background:linear-gradient(90deg,#5f7b5e 0%,#7a9a7c 50%,#7fb492 100%)"></div>

  <div class="photo" role="img" aria-label="Shingle roof valley covered in debris" style="left:53px;top:205px;background:linear-gradient(180deg,#6b6a5e 0%,#9a6850 40%,#a39a8a 70%,#8e5c48 100%)"></div>
  <div class="photo" role="img" aria-label="Roof valley being soft washed" style="left:225px;top:205px;background:linear-gradient(180deg,#7a7a70 0%,#a3705a 40%,#b07a63 100%)"></div>
  <div class="photo" role="img" aria-label="Gutter clogged with leaves" style="left:386px;top:205px;background:linear-gradient(180deg,#6e5a40 0%,#8a7358 50%,#5e4a35 100%)"></div>
  <div class="photo" role="img" aria-label="Clean empty gutter" style="left:558px;top:205px;background:linear-gradient(180deg,#55524e 0%,#6f6c68 45%,#b7b3a8 70%,#7b5d42 100%)"></div>

  <div class="divider" style="left:213px;top:205px;height:138px"></div>
  <div class="divider" style="left:546px;top:205px;height:138px"></div>
  <span class="tag" style="left:137px;top:331px">BEFORE</span>
  <span class="tag" style="left:226px;top:331px">AFTER</span>
  <span class="tag" style="left:470px;top:331px">BEFORE</span>
  <span class="tag" style="left:559px;top:331px">AFTER</span>

  <div class="phone" style="left:467px;top:356px;font-size:25px">
    <svg width="24" height="24" viewBox="0 0 32 32" style="margin-right:8px"><circle cx="16" cy="16" r="15" fill="var(--green)"/><path d="M11 8c1-.5 2 0 2.5 1l1.2 2.6c.3.8 0 1.6-.6 2l-1 .7c.8 1.9 2.3 3.5 4.2 4.4l.8-1c.5-.6 1.3-.8 2-.5l2.6 1.2c.9.5 1.3 1.5.9 2.4l-.5 1c-.6 1.2-2 1.8-3.3 1.4C14.6 22 10 17.4 8.9 12.2c-.3-1.3.2-2.7 1.4-3.4z" fill="var(--blue)"/></svg>
    415-362-0917
  </div>

  <div class="back-brand">
    <div class="name">Crestline</div>
    <div class="sub">Exterior Cleaning &amp; Maintenance Co.</div>
  </div>
</section>

</body>
</html>
```